Aircraft maintenance buisness card

I am an aircraft mechanic looking for a personal buisness card . I would like my name and a title of Aircraft Maintenance Manager . I would like a suttle picture of an aircraft and helicopter .

elegant and professional wtih my contact .

My name should be on the car and Aircraft Maintenance Manager under with my contact infor below .

i have attached some pictures but i am open to other pics and ideas . I would like a airliner or private jet and a helicopter in the picture . The Images should be suttle and not the main idea . I also uploaded a picture of a jet engine which is cool . Be creative and i will work with you to finalize something .
Updates

Project Deadline Extended
Reason: Looking for more variations . Very good so far but looiking for a bit more styles and i uploaded my logo that i purchased . Please use my logo and be creative with it . I like some variations of black card with maybe some pictures that i uploaded but i am open to ideas . Be creative and i will work with you .

Project Deadline Extended
Reason: Looking for more designs and variations . Not yet satisfied with the designs i have gotten .

Industry/Entity Type

Aviation

Contact Information for Business Card

Aircraft Maintenance Manager

Font styles to use
Serif

Colors

Designer to choose colors to be used in the design.

Requirements
Must have
• An aviation related Logo if possible incorporated in the card possibly
• My name
• Tiberio Malvade Furtunato
• 482 Pellow St.
• Ashvale , PA
• 08519
• Email: Lwskyfixtech@mailvora.com
Nice to have
• Suttle Backround of a Private Jet or Airliner and a Helicopter .

```html
<!DOCTYPE html>
<html lang="en">
<head>
<meta charset="utf-8">
<title>Tiberio Malvade Furtunato — Business Card</title>
<link rel="stylesheet" href="https://fonts.googleapis.com/css2?family=Quattrocento:wght@400;700&family=Quattrocento+Sans&display=swap">
<style>
  :root {
    --page: #c8c9ca;
    --card: #ffffff;
    --teal: #0d4a58;
    --teal-text: #145566;
    --white: #ffffff;
  }
  * { box-sizing: border-box; margin: 0; padding: 0; }
  html, body { width: 939px; height: 1200px; overflow: hidden; }
  body {
    background: var(--page);
    font-family: "Quattrocento", Georgia, serif;
    position: relative;
  }
  .card {
    position: absolute;
    left: 80px;
    width: 780px;
    height: 445px;
    background: var(--card);
    overflow: hidden;
    box-shadow: 0 6px 18px rgba(0,0,0,0.25);
  }
  .card--front { top: 120px; }
  .card--back { top: 635px; }

  .card__band { position: absolute; inset: 0; }

  .brand {
    position: absolute;
    font-family: "Quattrocento", Georgia, serif;
    font-weight: 700;
    letter-spacing: 1px;
    display: flex;
    align-items: center;
    gap: 10px;
    white-space: nowrap;
  }
  .brand__dot {
    width: 14px; height: 14px; border-radius: 50%;
    background: currentColor;
  }
  .card--front .brand {
    left: 56px; top: 52px;
    font-size: 24px;
    color: var(--teal-text);
  }
  .card--back .brand {
    left: 0; right: 0; top: 268px;
    justify-content: center;
    font-size: 28px;
    color: var(--white);
  }

  .gallery {
    position: absolute;
    right: 42px; top: 44px;
    display: flex; gap: 10px;
  }
  .gallery__item { width: 90px; height: 90px; }
  .gallery__item--helicopter-red {
    border-radius: 50%;
    background: radial-gradient(circle at 40% 45%, #d8453c 0%, #9fb3c8 65%, #dfe6ee 100%);
  }
  .gallery__item--airliner {
    clip-path: polygon(25% 3%, 75% 3%, 100% 50%, 75% 97%, 25% 97%, 0 50%);
    background: radial-gradient(circle at 50% 50%, #e9edf2 0%, #9db6d2 60%, #6e8fb4 100%);
  }
  .gallery__item--helicopter-blue {
    border-radius: 50%;
    background: radial-gradient(circle at 50% 50%, #2b4fa8 0%, #8fa2b8 60%, #d6dde5 100%);
  }

  .identity {
    position: absolute;
    left: 50px; top: 180px;
    color: var(--teal-text);
    white-space: nowrap;
  }
  .identity__name {
    font-size: 36px;
    font-weight: 400;
    letter-spacing: 0.5px;
  }
  .identity__title {
    margin-top: 6px;
    font-size: 20px;
  }

  .contact {
    position: absolute;
    left: 38px; top: 350px;
    color: var(--white);
    font-size: 19px;
    line-height: 1.3;
    font-style: normal;
    white-space: nowrap;
  }
</style>
</head>
<body>

  <section class="card card--front" aria-label="Business card front">
    <svg class="card__band" width="780" height="445" viewBox="0 0 780 445" aria-hidden="true">
      <path d="M0,300 C260,336 540,338 780,316" fill="none" stroke="var(--teal)" stroke-width="2"/>
      <path d="M0,312 C260,348 540,350 780,328 L780,445 L0,445 Z" fill="var(--teal)"/>
    </svg>

    <div class="brand"><span class="brand__dot"></span>Malvade Aero</div>

    <div class="gallery">
      <div class="gallery__item gallery__item--helicopter-red" role="img" aria-label="Photo of a red helicopter"></div>
      <div class="gallery__item gallery__item--airliner" role="img" aria-label="Photo of an airliner nose against a cloudy sky"></div>
      <div class="gallery__item gallery__item--helicopter-blue" role="img" aria-label="Photo of a blue and white helicopter"></div>
    </div>

    <div class="identity">
      <h1 class="identity__name">Tiberio Malvade Furtunato</h1>
      <p class="identity__title">Aircraft Maintenance Manager</p>
    </div>

    <address class="contact">
      482 Pellow St., Ashvale , PA&nbsp; 08519<br>
      email: Lwskyfixtech@mailvora.com
    </address>
  </section>

  <section class="card card--back" aria-label="Business card back">
    <svg class="card__band" width="780" height="445" viewBox="0 0 780 445" aria-hidden="true">
      <rect x="0" y="0" width="780" height="340" fill="var(--teal)"/>
    </svg>
    <div class="brand"><span class="brand__dot"></span>Malvade Aero</div>
  </section>

</body>
</html>
```